Valtrix PowerPoint Templates

We need a cover page and body page templates for a complete Powerpoint presentation. We administer workers' compensation claims in California mostly to public entities. We offer cloud based software to develop and communicate all the data for each claim. Although we are a technology company, we also see ourselves as the human interface working closely with the client and injured workers.
It all starts with our Logo!
We want to loosely relate our Powerpoint design with our Logo. Maybe just in the color! WE DONT WANT TO RECREATE OUR LOGO AS A PROPOSAL . I've posted the logo and a rough proposal page for reference. We designed it using ArtHive and feel the designer met our criteria very well. As I recall the spec for the logo was to use our name and incorporate "modern, professional and personal" into the design. We will use this template to attract new business. We will be approaching a variety of industries and want the template to be designed specifically for our business identity rather than for clients we are pursuing.
I will also post a simple example of a competitor's PowerPoint presentation for reference.
Please feel free to ask any questions you may have.
Thank You!
Gordon

Industry/Entity Type

Software

```html
<!DOCTYPE html>
<html lang="en">
<head>
<meta charset="utf-8">
<title>Valtrix – Presentation Cover</title>
<link rel="stylesheet" href="https://fonts.googleapis.com/css2?family=Mulish:wght@400;800&family=Roboto+Condensed:wght@400&family=Open+Sans:wght@400&display=swap">
<style>
  :root {
    --brand-blue: #2a5fb3;
    --hero-deep: #0b4aa8;
    --hero-mid: #1a5cbb;
    --hero-light: #3f7fd0;
    --title-grey: #a0a0a0;
    --body-grey: #666666;
    --footer-grey: #9b9b9b;
    --paper: #ffffff;
  }
  * { margin: 0; padding: 0; box-sizing: border-box; }
  html, body { width: 1200px; height: 900px; overflow: hidden; background: var(--paper); }
  .slide {
    position: relative;
    width: 1200px;
    height: 900px;
    background: var(--paper);
    font-family: "Mulish", sans-serif;
  }
  .hero {
    position: absolute;
    left: 0; top: 0;
    width: 1200px; height: 543px;
    background:
      radial-gradient(ellipse at 70% 45%, var(--hero-deep) 0%, transparent 55%),
      radial-gradient(ellipse at 20% 20%, var(--hero-light) 0%, transparent 60%),
      linear-gradient(135deg, var(--hero-mid) 0%, var(--hero-deep) 60%, var(--hero-mid) 100%);
  }
  .cover-title {
    position: absolute;
    left: 80px; top: 618px;
    font-weight: 800;
    font-size: 46px;
    letter-spacing: 0.5px;
    color: var(--title-grey);
  }
  .cover-title .accent { color: var(--brand-blue); }
  .cover-subtext {
    position: absolute;
    left: 80px; top: 690px;
    width: 460px;
    font-size: 17.5px;
    line-height: 29px;
    color: var(--body-grey);
  }
  .brand {
    position: absolute;
    left: 815px; top: 650px;
    width: 330px;
  }
  .brand-name {
    display: flex;
    align-items: center;
    gap: 16px;
    font-weight: 800;
    font-size: 66px;
    line-height: 1;
    color: var(--brand-blue);
  }
  .brand-dot {
    width: 22px; height: 22px;
    border-radius: 50%;
    background: var(--brand-blue);
  }
  .brand-tagline {
    margin-top: 10px;
    font-family: "Open Sans", sans-serif;
    font-size: 20px;
    color: #333333;
  }
  .footer {
    position: absolute;
    left: 0; top: 852px;
    width: 1200px; height: 48px;
    background: var(--footer-grey);
    display: flex;
    justify-content: space-between;
    align-items: center;
    padding: 0 12px;
    font-family: "Roboto Condensed", sans-serif;
    font-size: 20px;
    color: var(--paper);
  }
</style>
</head>
<body>
  <main class="slide">
    <div class="hero" role="img" aria-label="Abstract blue background of overlapping translucent triangles"></div>

    <h1 class="cover-title"><span class="accent">Project</span> TItle Here</h1>
    <p class="cover-subtext">Subtext here Subtext here Subtext here Subtext here Subtext here Subtext here Subtext here Subtext here</p>

    <div class="brand">
      <div class="brand-name"><span class="brand-dot"></span>Valtrix</div>
      <div class="brand-tagline">Claims Management Solutions</div>
    </div>

    <footer class="footer">
      <span class="copyright">Copyrightext text here</span>
      <span class="page-number">Page : 01</span>
    </footer>
  </main>
</body>
</html>
```